IT-support company web-site design

We need to re-design out site for existing clients and for the future promotions. Site needs to be attractive with intuitive interface. We need to keep our logo and colors but any reshuffles can be made. I provide the working site and re-made version, which we do nt like. It has to be more bright and clear. All the blocks have to be divided and look like logic and structured. PLease find the addresses to work with below.
The "real" one https://qorbil.com
The version http://tomuski.net/Qorbil/
If you have any с

Industry/Entity Type

It Company

Number of Pages Required

5+ page

Font styles to use
Sans Serif

Colors
9bcb3c

Requirements
Must have
• Our LOGO and our colors (green palette). We d like to make our services blocks as the main things. We need to have our images and slogans as there are extremely important advantages of our company.
Nice to have
• Original and modern view of the site.
Should not have
• unpredictable and @surprising@, hard- definable buttons and ways

```html
<!DOCTYPE html>
<html lang="en">
<head>
<meta charset="utf-8">
<title>Qorbil — IT Support</title>
<link href="https://fonts.googleapis.com/css2?family=Open+Sans:ital,wght@0,300;0,400;0,600;0,700;1,600;1,700&display=swap" rel="stylesheet">
<style>
:root{
  --mint:#80cfa6;
  --mint-dark:#5fb88c;
  --ink:#1e1f21;
  --ink-soft:#2c2d30;
  --text:#4a4a4a;
  --muted:#8a8a8a;
  --line:#d9d9d9;
  --field:#e6e6e6;
  --white:#ffffff;
}
*{box-sizing:border-box;margin:0;padding:0}
html,body{width:1200px;height:2602px;overflow:hidden}
body{position:relative;font-family:"Open Sans",Arial,sans-serif;color:var(--text);background:var(--white)}
.abs{position:absolute}

/* Header */
.site-header{position:absolute;left:0;top:0;width:1200px;height:140px;background:var(--ink)}
.brand{position:absolute;display:flex;align-items:center;gap:14px;color:var(--white);font-weight:300;letter-spacing:2px}
.brand-dot{border:3px solid var(--white);border-radius:50%}
.site-header .brand{left:45px;top:32px;font-size:40px}
.site-header .brand-dot{width:40px;height:40px}
.topbar{position:absolute;right:0;top:0;width:640px;height:46px;background:var(--mint);clip-path:polygon(30px 0,100% 0,100% 100%,0 100%);display:flex;align-items:center;justify-content:flex-end;gap:26px;padding-right:44px;color:var(--white);font-size:14px;font-weight:600}
.topbar .contact-item{display:flex;align-items:center;gap:8px}
.ico-circle{width:22px;height:22px;border-radius:50%;border:2px solid var(--white);display:inline-block}
.socials{display:flex;gap:6px}
.socials span{width:22px;height:22px;border-radius:50%;background:var(--white);opacity:.9}
.main-nav{position:absolute;right:34px;top:86px;display:flex;gap:22px;font-size:15px;font-weight:700;color:var(--white)}
.main-nav .active{color:var(--mint)}

/* Hero */
.hero{position:absolute;left:0;top:140px;width:1200px;height:550px;background:linear-gradient(100deg,#3f6a70 0%,#7fb2b2 35%,#a9d3cf 52%,#5f8e93 75%,#2f5056 100%)}
.hero-slogan{position:absolute;left:70px;top:235px;color:var(--white);font-size:29px;line-height:38px;font-weight:400;text-shadow:0 1px 3px rgba(0,0,0,.3)}
.contact-form{position:absolute;left:795px;top:75px;width:350px;height:395px;background:rgba(30,31,33,.82)}
.contact-form h3{height:40px;background:var(--mint);color:var(--white);font-size:17px;font-weight:700;letter-spacing:1px;text-align:center;line-height:40px}
.contact-form .fields{padding:14px 18px}
.dark-field{height:36px;background:#3a3b3e;border:1px solid #55565a;color:#c9c9c9;font-size:13px;padding:0 10px;line-height:34px;margin-bottom:9px}
.dark-field.row{display:flex;border:none;background:none;padding:0;gap:8px}
.dark-field.row div{flex:1;background:#3a3b3e;border:1px solid #55565a;padding:0 10px;position:relative}
.dark-field.row div.select::after{content:"";position:absolute;right:10px;top:14px;border:5px solid transparent;border-top-color:#c9c9c9}
.dark-field.message{height:150px}
.btn{display:inline-block;background:var(--mint);color:var(--white);font-weight:700;font-size:14px;letter-spacing:1px;text-align:center}
.contact-form .btn{width:105px;height:36px;line-height:36px}

/* Section headings */
.section-title{position:absolute;font-size:34px;font-weight:300;color:#333;text-align:center}
.section-title em{color:var(--mint);font-weight:700;font-style:italic}
.title-rule{position:absolute;height:1px;background:var(--line)}
.title-rule::after{content:"";position:absolute;left:50%;top:-7px;width:14px;height:14px;margin-left:-7px;border-radius:50%;border:2px solid var(--mint);background:var(--white)}

/* About */
.about-copy{position:absolute;left:90px;top:880px;width:540px;font-size:14.5px;line-height:22px;color:var(--text)}
.about-copy p{margin-bottom:18px}
.about .btn{position:absolute;left:90px;top:1118px;width:285px;height:52px;line-height:52px;font-size:14px}
.video{position:absolute;left:675px;top:882px;width:430px;height:315px;background:#e9e9e9;border:1px solid var(--line)}
.video-frame{width:100%;height:275px;background:radial-gradient(circle at 45% 45%,#3f7fb8 0%,#1b3e6b 55%,#0d1d36 100%)}
.video-bar{position:relative;height:38px;background:#e3e3e3}
.video-bar .play{position:absolute;left:12px;top:11px;border:8px solid transparent;border-left:12px solid #555}
.video-bar .track{position:absolute;left:42px;top:16px;width:280px;height:6px;background:#bcbcbc}
.video-bar .track span{display:block;width:110px;height:6px;background:#d6323b}
.video-bar .vol{position:absolute;left:340px;top:12px;width:30px;height:14px;background:#9a9a9a;clip-path:polygon(0 35%,35% 35%,70% 0,70% 100%,35% 65%,0 65%)}
.video-bar .full{position:absolute;right:14px;top:10px;width:18px;height:18px;border:3px solid #333}

/* Services */
.services{position:absolute;left:0;top:1262px;width:1200px;height:530px;background:linear-gradient(180deg,#6fbf98 0%,#8fd5b2 45%,#7ccaa2 100%)}
.services .section-title{color:var(--white);left:0;width:1200px;top:62px}
.services .section-title em{color:var(--white)}
.service{position:absolute;width:270px;color:var(--white)}
.service h4{font-size:16px;font-weight:700;margin-bottom:4px}
.service p{font-size:12.5px;line-height:17px}
.service.right{text-align:left}
.service-icon{position:absolute;width:64px;height:64px;border-radius:50%;border:2px solid rgba(255,255,255,.85);background:rgba(255,255,255,.12)}
.hub{position:absolute;left:510px;top:270px;width:180px;height:180px;border-radius:50%;border:7px solid var(--white);display:flex;align-items:center;justify-content:center;color:var(--white);font-size:28px;font-weight:300;letter-spacing:2px}

/* News and message */
.news-item{position:absolute;left:90px;width:560px;height:90px}
.date{position:absolute;left:0;top:0;width:62px;height:78px;background:#d7d7d7;text-align:center;color:var(--white)}
.date b{display:block;font-size:28px;line-height:32px;padding-top:6px}
.date small{display:block;font-size:10px;font-weight:700;letter-spacing:1px}
.date i{position:absolute;left:0;bottom:-16px;width:62px;height:22px;background:var(--mint);font-style:normal;font-size:12px;font-weight:700;line-height:22px}
.news-body{position:absolute;left:95px;top:0;width:330px}
.news-body h5{font-size:13px;font-weight:700;color:#333;margin-bottom:3px}
.news-body p{font-size:12.5px;line-height:16px;color:var(--text)}
.light-field{position:absolute;left:775px;width:310px;background:var(--field);border:1px solid #d2d2d2;font-size:11px;color:#777;padding:4px 8px}
.dark-btn{position:absolute;left:775px;width:150px;height:32px;background:#555658;color:var(--white);font-size:14px;font-weight:700;text-align:center;line-height:32px;letter-spacing:1px}

/* Footer */
.site-footer{position:absolute;left:0;top:2262px;width:1200px;height:293px;background:var(--mint);color:var(--white)}
.site-footer .brand{left:45px;top:115px;font-size:44px}
.site-footer .brand-dot{width:44px;height:44px}
.footer-col{position:absolute;top:45px;font-size:13px;line-height:21px}
.footer-col h6{font-size:14px;font-weight:700;letter-spacing:1px;margin-bottom:10px;padding-bottom:6px;border-bottom:1px solid rgba(255,255,255,.6);width:160px}
.footer-col .line{display:flex;gap:8px;align-items:flex-start;margin-bottom:6px}
.map{position:absolute;left:765px;top:38px;width:322px;height:200px;background:linear-gradient(135deg,#eef0ea 0%,#dfe4da 100%)}
.copyright{position:absolute;left:0;top:2555px;width:1200px;height:47px;background:var(--ink-soft);color:#cfcfcf;font-size:11px;letter-spacing:.5px;line-height:47px;padding-left:45px}
.copyright .socials{position:absolute;right:40px;top:13px}
.copyright .socials span{background:#e9e9e9}
</style>
</head>
<body>

<header class="site-header">
  <div class="brand"><span class="brand-dot"></span>QORBIL</div>
  <div class="topbar">
    <span class="contact-item">
      <svg width="20" height="20" viewBox="0 0 20 20"><circle cx="10" cy="10" r="9" fill="none" stroke="#fff" stroke-width="2"/><path d="M7 5.5c-.7.5-1 1.4-.6 2.5.8 2 2.4 3.7 4.5 4.7 1 .4 1.9.2 2.5-.5l-1.6-1.5-1.2.6c-.9-.5-1.7-1.3-2.2-2.2l.6-1.2z" fill="#fff"/></svg>
      (555) 318-2740
    </span>
    <span class="contact-item">
      <svg width="20" height="20" viewBox="0 0 20 20"><circle cx="10" cy="10" r="9" fill="none" stroke="#fff" stroke-width="2"/><rect x="5.5" y="7" width="9" height="6.5" fill="none" stroke="#fff" stroke-width="1.4"/><path d="M5.5 7l4.5 3.5L14.5 7" fill="none" stroke="#fff" stroke-width="1.4"/></svg>
      info@qorbil.com
    </span>
    <span class="socials"><span></span><span></span><span></span><span></span></span>
  </div>
  <nav class="main-nav">
    <span class="active">Home</span><span>Qorbil Difference</span><span>Services</span><span>Customers</span><span>Resources</span><span>Support</span><span>About</span><span>Contact</span>
  </nav>
</header>

<section class="hero" role="img" aria-label="City skyline at dusk with light trails along a highway, tinted teal">
  <h1 class="hero-slogan">We Make Your Information Technology<br>SECURE and SIMPLE</h1>
  <form class="contact-form">
    <h3>CONTACT US TODAY</h3>
    <div class="fields">
      <div class="dark-field">Name</div>
      <div class="dark-field">Email Address</div>
      <div class="dark-field row"><div>Phone</div><div class="select">Services</div></div>
      <div class="dark-field message">Message</div>
      <span class="btn">SUBMIT</span>
    </div>
  </form>
</section>

<section class="about">
  <h2 class="section-title" style="left:0;width:1200px;top:760px">About <em>QORBIL</em></h2>
  <div class="title-rule" style="left:470px;top:832px;width:260px"></div>
  <div class="about-copy">
    <p>Lorem ipsum dolor sit amet, consectetuer adipiscing elit, sed diam nonummy nibh euismod tincidunt ut laoreet dolore magna aliquam erat volutpat. Ut wisi enim ad minim veniam, quis nostrud exerci tation ullamcorper suscipit lobortis nisl ut aliquip ex ea commodo consequat.</p>
    <p>Duis autem vel eum iriure dolor in hendrerit in vulputate velit esse molestie consequat, vel illum dolore eu feugiat nulla facilisis at vero eros et accumsan et iusto odio dignissim qui blandit praesent luptatum zzril delenit augue duis dolore te feugait nulla facilisi.</p>
  </div>
  <span class="btn">DISCOVER MORE ABOUT US</span>
  <div class="video">
    <div class="video-frame" role="img" aria-label="Video still of a hand touching a glowing network of technology icons"></div>
    <div class="video-bar"><span class="play"></span><span class="track"><span></span></span><span class="vol"></span><span class="full"></span></div>
  </div>
</section>

<section class="services" role="img" aria-label="Aerial city highway interchange at night under a mint green overlay">
  <h2 class="section-title">Our <em>Services</em></h2>
  <div class="title-rule" style="left:520px;top:130px;width:160px;background:rgba(255,255,255,.6)"></div>

  <div class="service" style="left:40px;top:188px">
    <h4>Upfront Audit</h4>
    <p>Lorem ipsum dolor sit amet, consectetuer adipiscing elit, sed diam nonummy aliquam erat volutpat. Ut wisi enim ad minim veniam, quis nostrud exerci.</p>
  </div>
  <span class="service-icon" style="left:320px;top:200px"></span>

  <div class="service" style="left:905px;top:188px">
    <h4>Cost Savings</h4>
    <p>Lorem ipsum dolor sit amet, consectetuer adipiscing elit, sed diam nonummy aliquam erat volutpat. Ut wisi enim ad minim veniam, quis nostrud exerci.</p>
  </div>
  <span class="service-icon" style="left:818px;top:200px"></span>

  <div class="service" style="left:40px;top:372px">
    <h4>Moving to Qorbil System</h4>
    <p>Lorem ipsum dolor sit amet, consectetuer adipiscing elit, sed diam nonummy aliquam erat volutpat. Ut wisi enim ad minim veniam, quis nostrud exerci.</p>
  </div>
  <span class="service-icon" style="left:320px;top:382px"></span>

  <div class="service" style="left:905px;top:372px">
    <h4>Performance Tracking</h4>
    <p>Lorem ipsum dolor sit amet, consectetuer adipiscing elit, sed diam nonummy aliquam erat volutpat. Ut wisi enim ad minim veniam, quis nostrud exerci.</p>
  </div>
  <span class="service-icon" style="left:818px;top:382px"></span>

  <div class="hub">QORBIL</div>
</section>

<section class="news">
  <h2 class="section-title" style="left:90px;width:560px;top:1855px">Latest <em>News</em></h2>
  <div class="title-rule" style="left:250px;top:1922px;width:240px"></div>

  <article class="news-item" style="top:1990px">
    <div class="date"><b>01</b><small>SEP</small><i>2017</i></div>
    <div class="news-body">
      <h5>Nam liber tempor cum soluta nobis</h5>
      <p>Lorem ipsum dolor sit amet, consectetuer adipiscing elit, sed diam nonummy nibh euismod tincidunt ut laoreet dolore magna aliquam erat.</p>
    </div>
  </article>
  <article class="news-item" style="top:2122px">
    <div class="date"><b>24</b><small>AUG</small><i>2017</i></div>
    <div class="news-body">
      <h5>Nam liber tempor cum soluta nobis</h5>
      <p>Lorem ipsum dolor sit amet, consectetuer adipiscing elit, sed diam nonummy nibh euismod tincidunt ut laoreet dolore magna aliquam erat.</p>
    </div>
  </article>
</section>

<section class="message">
  <h2 class="section-title" style="left:740px;width:380px;top:1855px">Send Us a <em>Message</em></h2>
  <div class="title-rule" style="left:810px;top:1922px;width:240px"></div>
  <div class="light-field" style="top:1990px;height:28px">Name</div>
  <div class="light-field" style="top:2026px;height:28px">Email</div>
  <div class="light-field" style="top:2062px;height:72px">Message</div>
  <div class="dark-btn" style="top:2142px">SUBMIT</div>
</section>

<footer class="site-footer">
  <div class="brand"><span class="brand-dot"></span>QORBIL</div>
  <div class="footer-col" style="left:375px">
    <h6>QUICK LINKS</h6>
    Home<br>About<br>Services<br>Projects<br>News<br>Contact
  </div>
  <div class="footer-col" style="left:545px">
    <h6>CONTACT</h6>
    <div class="line">
      <svg width="12" height="16" viewBox="0 0 12 16"><path d="M6 0a6 6 0 0 0-6 6c0 4.5 6 10 6 10s6-5.5 6-10a6 6 0 0 0-6-6zm0 8.5A2.5 2.5 0 1 1 6 3.5a2.5 2.5 0 0 1 0 5z" fill="#fff"/></svg>
      <span>Qorbil<br>48 Larkfield Avenue<br>Brookvale, TX 75510</span>
    </div>
    <div class="line">
      <svg width="14" height="14" viewBox="0 0 14 14"><path d="M3 .5c-1 .6-1.6 2-1 3.5 1.3 3.2 3.9 5.8 7 7 1.6.6 2.9 0 3.5-1L10 7.5 8.2 8.5C6.8 7.8 5.8 6.8 5 5.3L6 3.5z" fill="#fff"/></svg>
      <span>(555) 318-2740</span>
    </div>
    <div class="line">
      <svg width="14" height="12" viewBox="0 0 14 12"><rect x="1" y="1" width="12" height="10" fill="none" stroke="#fff" stroke-width="1.5"/><path d="M1 1l6 5 6-5" fill="none" stroke="#fff" stroke-width="1.5"/></svg>
      <span>info@qorbil.com</span>
    </div>
  </div>
  <div class="map" role="img" aria-label="Street map showing the office location"></div>
</footer>

<div class="copyright">COPYRIGHT © 2017 QORBIL. ALL RIGHTS RESERVED.
  <span class="socials"><span></span><span></span><span></span></span>
</div>

</body>
</html>
```